St Velor 43rd Festival

We need a poster design for the 43rd St Velor Youth Festival.
The festival will include a church service, folkloric dancing and a live band. The poster will be primarily in the Cyrillic language so it will need to be editable by us to confirm the writing.
I have attached a older design that we would like to use as a base. The new look of the poster is to be fresh and clean, i have attached an example of the new / clean poster. We would like to incorporate our countries nations colours, red, blue and white like in the example.

You will have to extract the text from the scanned 'old poster' pdf document

I have marked up a image 'my thoughts' to help

Once this poster is finalised we will engage with you further for to design menu poster, entry ticket design etc.

```html
<!DOCTYPE html>
<html lang="sr">
<head>
<meta charset="utf-8">
<title>St Velor 43rd Festival</title>
<link href="https://fonts.googleapis.com/css2?family=Open+Sans:wght@600;700;800&family=Noto+Serif:ital,wght@1,700&display=swap" rel="stylesheet">
<style>
  :root{
    --red:#b5202b;
    --red-deep:#8e1620;
    --blue:#1f3a70;
    --blue-deep:#132a57;
    --white:#ffffff;
    --ink:#1c1c1c;
    --page:#e9e7e4;
  }
  *{box-sizing:border-box;margin:0;padding:0}
  html,body{width:1200px;height:1117px;overflow:hidden;background:var(--page);font-family:"Open Sans",sans-serif}
  .poster{position:absolute;left:210px;top:8px;width:779px;height:1100px;background:var(--white);overflow:hidden}
  .abs{position:absolute}
  .header-band{left:0;top:0;width:400px;height:111px;background:var(--red)}
  .header-text{left:50px;top:25px;width:350px;color:var(--white);font-weight:700;font-size:13px;line-height:15.8px;white-space:nowrap}
  .church-photo{left:395px;top:0;width:384px;height:430px;background:linear-gradient(180deg,#c9d3dc 0%,#c98a5e 45%,#a8683f 80%,#7e8a52 100%)}
  .arc{left:0;top:0;width:779px;height:560px}
  .title{left:56px;top:132px;color:var(--blue-deep);font-weight:700;font-size:29px;line-height:30px;letter-spacing:.2px}
  .title .accent{display:block;color:var(--red);font-size:45px;line-height:52px;margin-top:2px}
  .folk-photo{left:0;top:299px;width:350px;height:137px;background:linear-gradient(180deg,#6a8aa6 0%,#8a3b45 45%,#2a2a2e 100%)}
  .band-photo{left:355px;top:177px;width:262px;height:262px;border-radius:50%;background:linear-gradient(160deg,#3c3c40 0%,#d9d4cc 50%,#d64a5a 100%);border:7px solid var(--white)}
  .flag-red{left:0;top:435px;width:779px;height:169px;background:linear-gradient(100deg,var(--red-deep),var(--red) 40%,#c7303a 70%,var(--red-deep))}
  .flag-blue{left:0;top:604px;width:779px;height:188px;background:linear-gradient(100deg,var(--blue-deep),var(--blue) 50%,var(--blue-deep))}
  .flag-white{left:0;top:792px;width:779px;height:308px;background:linear-gradient(180deg,#f2f2f4,#ffffff 40%)}
  .emblem{left:34px;top:455px;width:250px;height:430px;border-radius:10px 10px 125px 125px;background:linear-gradient(180deg,#d6a53c 0%,#c7303a 30%,#f2f2f2 60%,#c7303a 100%)}
  .food-photo{left:0;top:880px;width:430px;height:220px;border-radius:0 230px 0 0;background:linear-gradient(160deg,#e8e4df 0%,#8a4a2a 40%,#5e2e18 100%)}
  .title-pill{left:305px;top:463px;width:423px;height:60px;border-radius:30px;background:var(--white);box-shadow:0 3px 8px rgba(0,0,0,.35);text-align:center;padding-top:4px}
  .title-pill .en{font-family:"Noto Serif",serif;font-style:italic;font-weight:700;font-size:26px;line-height:32px;color:var(--red);white-space:nowrap}
  .title-pill .venue{font-size:11px;font-weight:600;color:var(--blue-deep);display:flex;justify-content:center;align-items:center;gap:5px;white-space:nowrap}
  .date-pill{left:301px;width:182px;height:60px;border-radius:30px;border:3px solid var(--white);color:var(--white);font-weight:700;font-size:16.5px;line-height:18px;padding:10px 0 0 28px;box-shadow:0 3px 6px rgba(0,0,0,.3);white-space:nowrap}
  .date-pill.red{top:541px;background:var(--red)}
  .date-pill.blue{top:696px;background:var(--blue)}
  .date-pill.navy{top:820px;height:54px;background:var(--blue);border-color:transparent;padding-top:9px}
  .rule{left:470px;width:309px;height:3px;background:var(--white)}
  .rule.navy{background:var(--blue)}
  .schedule{left:502px;font-weight:700;font-size:13.6px;line-height:16.5px;white-space:nowrap}
  .schedule.friday{top:557px;color:var(--white)}
  .schedule.saturday{top:618px;color:var(--white)}
  .schedule.sunday{top:807px;color:var(--ink)}
  .schedule .time{color:var(--red)}
  .schedule .indent{padding-left:42px}
  .welcome{left:435px;top:908px;width:316px;text-align:center;font-weight:700;font-size:11.8px;line-height:17.5px;color:var(--ink)}
  .info-label{left:435px;top:1012px;width:316px;text-align:center;font-weight:700;font-size:12.4px;color:var(--red);white-space:nowrap}
  .phone-pill{left:447px;top:1033px;width:292px;height:36px;border-radius:18px;background:var(--red);color:var(--white);font-weight:700;font-size:21px;line-height:1;white-space:nowrap;display:flex;align-items:center;justify-content:center;gap:6px}
  .bottom-bar{left:0;top:1024px;width:413px;height:76px;background:var(--blue)}
  .bottom-text{left:0;top:1040px;width:413px;text-align:center;color:var(--white);font-weight:700;font-size:13.6px;line-height:17px}
</style>
</head>
<body>
<div class="poster">
  <div class="abs church-photo" role="img" aria-label="Photograph of a brick-striped Orthodox church under a cloudy sky"></div>
  <svg class="abs arc" viewBox="0 0 779 560" aria-hidden="true">
    <path d="M432 0 C 360 80, 360 240, 410 310" fill="none" stroke="var(--white)" stroke-width="30"/>
    <path d="M455 0 C 385 80, 380 220, 420 300" fill="none" stroke="var(--blue)" stroke-width="12"/>
    <path d="M560 405 C 640 430, 720 420, 779 380 L779 560 L520 560 Z" fill="var(--white)"/>
    <path d="M565 400 C 650 420, 725 405, 779 370" fill="none" stroke="var(--blue)" stroke-width="12"/>
  </svg>
  <div class="abs header-band"></div>
  <p class="abs header-text">Организациони одбор Православне Епархије<br>Велорске са благословом нашег Преосвећеног<br>Владике Господина Доротеја организује и<br>позива на</p>
  <h1 class="abs title">ЧЕТРДЕСЕТ ТРЕЋИ<br>СВЕТОВЕЛОРСКИ<br>ОМЛАДИНСКИ<span class="accent">ФЕСТИВАЛ</span></h1>

  <div class="abs flag-red"></div>
  <div class="abs flag-blue"></div>
  <div class="abs flag-white"></div>
  <div class="abs folk-photo" role="img" aria-label="Photograph of a folklore ensemble in traditional costume on stage"></div>
  <div class="abs band-photo" role="img" aria-label="Photograph of the festival band members"></div>
  <div class="abs emblem" role="img" aria-label="National coat of arms"></div>
  <div class="abs food-photo" role="img" aria-label="Photograph of a plate of grilled meat with salad"></div>

  <div class="abs title-pill">
    <div class="en">43nd St. Velor Youth Festival</div>
    <div class="venue">
      <svg width="13" height="13" viewBox="0 0 24 24" aria-hidden="true"><circle cx="12" cy="12" r="11" fill="var(--blue-deep)"/><path d="M12 5a4.5 4.5 0 0 0-4.5 4.5c0 3.4 4.5 8.5 4.5 8.5s4.5-5.1 4.5-8.5A4.5 4.5 0 0 0 12 5z" fill="var(--white)"/><circle cx="12" cy="9.5" r="1.7" fill="var(--blue-deep)"/></svg>
      Манастир Нова Обала, 120 Ridgeline Road - BRANFORD - ACT 2699
    </div>
  </div>

  <div class="abs rule" style="top:597px"></div>
  <div class="abs date-pill red">ПЕТАК - 26<br>ЈАНУАР 2024.</div>
  <div class="abs schedule friday">18.00 Часова Вечерње<br><span class="indent">Богослужење</span></div>

  <div class="abs rule" style="top:752px"></div>
  <div class="abs date-pill blue">СУБОТА 27.<br>ЈАНУАР 2024.</div>
  <div class="abs schedule saturday">
    10.00 Света Архијерејска<br><span class="indent">Литургија</span><br>
    12.30 Отварање Фестивала<br>
    13.00 Наступи фолклорних група<br><span class="indent">и народно весеље</span><br>
    18.00 Вечерње Богослужење
  </div>

  <div class="abs rule navy" style="top:868px"></div>
  <div class="abs date-pill navy">НЕДЕЉА - 28.<br>ЈАНУАР 2024.</div>
  <div class="abs schedule sunday">
    <span class="time">10.00</span> Света Литургија<br>
    <span class="time">11.30</span> Наставак фолклорних група<br>
    <span class="time">16.00</span> Завршетак Фестивала
  </div>

  <p class="abs welcome">ДОБРО НАМ ДОШЛИ У СВЕТОВЕЛОРСКУ СВЕТИЊУ СВИХ ВЕРНИХ ЈУЖНИХ КРАЈЕВА И ОСТРВА. И НА ПОКЛОЊЕЊЕ НЕДАВНО ПРИСТИГЛОЈ ИЗ МАНАСТИРА СВЕТОГ ЈОВАНА СВЕТОЈ ИКОНИ БОГОРОДИЦИ ТРОЈЕРУЧИЦИ!</p>
  <p class="abs info-label">ЗА СВЕ ИНФОРМАЦИ ІТЕ СЕ НА TEL:</p>
  <div class="abs phone-pill">
    <svg width="18" height="18" viewBox="0 0 24 24" aria-hidden="true"><circle cx="12" cy="12" r="11" fill="var(--white)"/><path d="M8.6 6.5l1.6 2.4-1 1.3a8 8 0 0 0 4.6 4.6l1.3-1 2.4 1.6-.7 2c-5.3.2-10-4.5-9.8-9.8z" fill="var(--red)"/></svg>
    <span>0400111 0400 222 333</span>
  </div>

  <div class="abs bottom-bar"></div>
  <p class="abs bottom-text">ЧЕКА ВАС ДОМАЋИНСКА КУХИЊА<br>ПРИЈАТНА СРПСКА МУЗИКА</p>
</div>
</body>
</html>
```